LEARN Business Skills so you can Earn a good living

size of the poster is 8”x 10.75" plus 0.25" bleed.
Please leave 1 inch on the bottoum for footer
I want a design a poster that will attract people's attention.
I appreciate a creative ad however the ad should not take away from being able to clearly read the text.
-I also appreciate a simple creative ad that is not too busy.
-you can use graphics, vectors, or pictures of real people.
-however, if you use real people it should be a white male that is wearing a white shirt and look like a professional person.

Target Market(s)

Potential young business people

Industry/Entity Type

education

Requirements
Must have
• easy to read the text
Nice to have
• I would like a "creative" simple ad that is easy to be read
Should not have
• pictures of women

```html
<!DOCTYPE html>
<html lang="en">
<head>
<meta charset="utf-8">
<title>Learn It to Earn It — Business Enrichment Course</title>
<link rel="stylesheet" href="https://fonts.googleapis.com/css2?family=Montserrat:wght@400;700;800&family=Great+Vibes&display=swap">
<style>
  :root {
    --page-bg: #8c8c8c;
    --ink-white: #ffffff;
    --photo-dark: #141414;
    --photo-mid: #2b2b2b;
    --band-top: #5d6162;
    --band-mid: #3a3c3c;
    --band-bottom: #0e0d0c;
    --footer: #ffffff;
  }
  * { margin: 0; padding: 0; box-sizing: border-box; }
  html, body {
    width: 1200px; height: 1200px; overflow: hidden;
    background: var(--page-bg);
  }
  .poster {
    position: absolute; left: 169px; top: 30px;
    width: 862px; height: 1140px;
    overflow: hidden;
    font-family: "Montserrat", Arial, sans-serif;
    color: var(--ink-white);
  }
  .hero-photo {
    position: absolute; left: 0; top: 0; width: 862px; height: 517px;
    background:
      radial-gradient(ellipse 210px 300px at 560px 300px, #d8d8d8 0%, #9a9a9a 45%, rgba(40,40,40,0) 100%),
      radial-gradient(ellipse 520px 380px at 30% 40%, var(--photo-mid), var(--photo-dark));
  }
  .info-band {
    position: absolute; left: 0; top: 517px; width: 862px; height: 522px;
    background: linear-gradient(180deg, var(--band-top) 0%, var(--band-mid) 45%, #222 75%, var(--band-bottom) 100%);
  }
  .footer-space {
    position: absolute; left: 0; top: 1039px; width: 862px; height: 101px;
    background: var(--footer);
  }
  .headline {
    position: absolute; left: 88px;
    font-weight: 800; font-size: 140px; line-height: 1;
    letter-spacing: -2px; white-space: nowrap;
    text-shadow: 0 8px 14px rgba(0,0,0,0.45);
  }
  .headline--learn { top: 395px; }
  .headline--earn { top: 524px; left: 178px; }
  .headline-joiner {
    position: absolute; left: 80px; top: 556px;
    font-family: "Great Vibes", cursive;
    font-size: 96px; line-height: 1;
    text-shadow: 0 6px 10px rgba(0,0,0,0.4);
  }
  .course-title {
    position: absolute; right: 473px; top: 691px;
    text-align: right; font-weight: 700;
    font-size: 44px; line-height: 47px; letter-spacing: -0.5px;
  }
  .course-tagline {
    position: absolute; right: 473px; top: 837px;
    text-align: right; font-weight: 400;
    font-size: 14px; line-height: 20px;
  }
  .benefits-label {
    position: absolute; left: 466px; top: 698px;
    font-size: 14px; line-height: 20px; font-weight: 400;
  }
  .benefits {
    position: absolute; left: 466px; top: 720px; width: 330px;
    font-weight: 700; font-size: 28px; line-height: 39px; letter-spacing: -0.3px;
  }
  .topics {
    position: absolute; left: 82px; top: 924px; width: 720px;
    font-weight: 700; font-size: 10.5px; line-height: 19px;
    text-transform: uppercase; white-space: nowrap;
  }
</style>
</head>
<body>
  <main class="poster">
    <div class="hero-photo" role="img" aria-label="Photograph of a professional man in a white shirt typing on a silver laptop against a dark textured wall"></div>
    <div class="info-band"></div>
    <div class="footer-space"></div>

    <h1>
      <span class="headline headline--learn">LEARN IT</span>
      <span class="headline-joiner">to</span>
      <span class="headline headline--earn">EARN IT</span>
    </h1>

    <h2 class="course-title">Business<br>Enrichment<br>Course</h2>
    <p class="course-tagline">A proven success of helping<br>people in their livelihoods</p>

    <p class="benefits-label">Business skills that will help you:</p>
    <p class="benefits">Get a quality job -<br>start / grow your<br>business-Increase<br>your salary</p>

    <p class="topics">
      Business Admiistration – Small Business Management -<br>
      Finance - Investments - Computers- Accounting - Sales&nbsp; Marketing - Project Management Interviewing<br>
      Skills - Business Law -Negotiation – Public Speaking - Import/Export - Information Technoloy -<br>
      Distribution - Marketing -&nbsp;&nbsp; Ledgerly - Real Estate - Health Care-Management - Rivermart
    </p>
  </main>
</body>
</html>
```